Korvane Supplies Ltd Stationery Design Project

hi we need to design business cards, letter head, complimentary slips, scribble pads, note pads, envelopes for korvane supplies ltd.

please see business cards details

Tobias Welkerin

P.O Box 41823 -00719 Nairobi - Kenya
Tel: +254-733-182-947
Email: korvanesupplies@brelomail.test

company name should appear on all stationery : Korvane Supplies Ltd

Industry/Entity Type

Business

Requirements
Must have
• kindly stick to colours in the logo

```html
<!DOCTYPE html>
<html lang="en">
<head>
<meta charset="UTF-8">
<title>Korvane Supplies Ltd – Scribble Pad and Note Pad</title>
<link href="https://fonts.googleapis.com/css2?family=Russo+One&display=swap" rel="stylesheet">
<style>
  :root {
    --backdrop: #dedede;
    --paper: #ffffff;
    --brand-navy: #2b3a8f;
    --brand-orange: #ee8a1c;
    --brand-yellow: #f2d23a;
    --paper-edge: #cfcfcf;
  }
  * { margin: 0; padding: 0; box-sizing: border-box; }
  html, body {
    width: 1200px;
    height: 870px;
    overflow: hidden;
    background: var(--backdrop);
  }
  .canvas {
    position: relative;
    width: 1200px;
    height: 870px;
  }
  .pad {
    position: absolute;
    background: var(--paper);
    border: 1px solid var(--paper-edge);
    overflow: hidden;
  }
  .scribble-pad { left: 212px; top: 140px; width: 394px; height: 565px; }
  .note-pad { left: 730px; top: 122px; width: 242px; height: 244px; }

  .brand {
    position: absolute;
    left: 0; right: 0;
    display: flex;
    flex-direction: column;
    align-items: center;
    font-family: "Russo One", sans-serif;
    color: var(--brand-navy);
    line-height: 1;
    text-transform: uppercase;
  }
  .brand-dot {
    border-radius: 50%;
    background: var(--brand-orange);
  }
  .scribble-pad .brand { top: 58px; }
  .scribble-pad .brand-dot { width: 28px; height: 28px; margin-bottom: 10px; }
  .scribble-pad .brand-name { font-size: 31px; letter-spacing: 1px; }
  .scribble-pad .brand-sub { font-size: 17px; letter-spacing: 2px; margin-top: 3px; }

  .note-pad .brand { top: 14px; }
  .note-pad .brand-dot { width: 14px; height: 14px; margin-bottom: 5px; }
  .note-pad .brand-name { font-size: 16px; letter-spacing: 0.5px; }
  .note-pad .brand-sub { font-size: 9px; letter-spacing: 1px; margin-top: 2px; }

  .wave-band {
    position: absolute;
    left: 0; bottom: 0;
    width: 100%;
    display: block;
  }
</style>
</head>
<body>
<main class="canvas">

  <section class="pad scribble-pad" aria-label="Scribble pad">
    <div class="brand">
      <span class="brand-dot"></span>
      <span class="brand-name">Korvane</span>
      <span class="brand-sub">Supplies</span>
    </div>
    <svg class="wave-band" viewBox="0 0 394 60" height="60" preserveAspectRatio="none" aria-hidden="true">
      <defs>
        <linearGradient id="band-large" x1="0" x2="1" y1="0" y2="0">
          <stop offset="0" stop-color="var(--brand-yellow)"/>
          <stop offset="1" stop-color="var(--brand-orange)"/>
        </linearGradient>
      </defs>
      <path d="M0 2 Q 150 24 394 10 L394 13 Q 150 26 0 7 Z" fill="var(--brand-orange)"/>
      <path d="M0 14 Q 160 26 394 16 L394 60 L0 60 Z" fill="url(#band-large)"/>
    </svg>
  </section>

  <section class="pad note-pad" aria-label="Note pad">
    <div class="brand">
      <span class="brand-dot"></span>
      <span class="brand-name">Korvane</span>
      <span class="brand-sub">Supplies</span>
    </div>
    <svg class="wave-band" viewBox="0 0 242 38" height="38" preserveAspectRatio="none" aria-hidden="true">
      <defs>
        <linearGradient id="band-small" x1="0" x2="1" y1="0" y2="0">
          <stop offset="0" stop-color="var(--brand-yellow)"/>
          <stop offset="1" stop-color="var(--brand-orange)"/>
        </linearGradient>
      </defs>
      <path d="M0 1 Q 100 13 242 7 L242 9 Q 100 15 0 5 Z" fill="var(--brand-orange)"/>
      <path d="M0 9 Q 110 16 242 11 L242 38 L0 38 Z" fill="url(#band-small)"/>
    </svg>
  </section>

</main>
</body>
</html>
```